Ledgerly Swift GUI Contest

Hello everyone. I want a unique design for my app "Ledgerly Swift". Now, I published this app to Pixel Bazaar.

(Please see https://apps.pixelbazaar-demo.net/store/apps/details?id=com.mornvale.ledgerlyswift&feature=search_result#?t=QXBwUGFnZVZpZXdJbnZlbnRlZEV4YW1wbGVTdHJpbmdGb3JUZXN0aW5nT25seQ )

Now, I got a lot of negative responds for UI. So, I really need beautiful UI for this app.

Please see attachment. I like that kind of framework.

I don't like Side by Side display. I like Currency and Country shows vertically.

I will add Banner at the bottom of screen too. So, make sure give enough space for banner ,if not your UI design will be ugly due to this.

Please see my attached files. These are screenshots of my current UI design for Ledgerly Swift. You can reference these screenshots if you don't have android devices to test.

Rotate icon at the center of screen is to reverse country. :)

Target Market(s)

Android

Industry/Entity Type

Store

Requirements
Must have
• Colorful
Screen Size (320 x 480 or 480 x 800 or 480 x 854 or 1280 x 720 and 1280 x 800)
Nice to have
• I attached sample template file. I don't mean that UI design may be similar like this. You can design as you like. You can use any color. If it is beautiful in my eye, I will choose. If I like two designs, I will choose 2nd winner too.

I really need eye catching design.
Should not have
• I hate Side by Side currency display. (https://apps.pixelbazaar-demo.net/store/apps/details?id=com.brisk.tally.plus.quorvix&feature=search_result#?t=SW52ZW50ZWRQbGFjZWhvbGRlclRva2VuRm9yU2Vjb25kQXBwTGlua0V4YW1wbGU.)

```html
<!DOCTYPE html>
<html lang="en">
<head>
<meta charset="utf-8">
<title>Ledgerly Swift – screen sizes</title>
<link href="https://fonts.googleapis.com/css2?family=Questrial&family=Mulish:wght@700;900&family=Montserrat:wght@700&display=swap" rel="stylesheet">
<style>
  :root{
    --page:#ffffff;
    --ink:#111111;
    --panel:#313131;
    --panel-dark:#262626;
    --bar-top:#5a5a5a;
    --bar-bottom:#343434;
    --gold:#f5b400;
    --label:#c9c9c9;
    --row-text:#ececec;
    --date:#1e9fe6;
    --digits:#e9e9e9;
    --ad-dark:#2c2c2c;
    --ad-lime:#b9d531;
    --ad-pink:#cc0a66;
  }
  html,body{margin:0;padding:0;background:var(--page);}
  body{width:1200px;height:901px;overflow:hidden;position:relative;font-family:"Questrial",sans-serif;}

  .size-title{position:absolute;top:72px;margin:0;font-family:"Montserrat",sans-serif;font-weight:700;font-size:26px;color:var(--ink);text-align:center;line-height:32px;}

  .screen{position:absolute;top:147px;overflow:hidden;background:var(--panel);}
  .screen--1280{left:32px;width:383px;height:681px;}
  .screen--854{left:442px;width:255px;height:454px;}
  .screen--800{left:722px;width:255px;height:424px;}
  .screen--480{left:998px;width:171px;height:256px;}

  .toolbar{position:absolute;left:0;right:0;top:0;display:flex;background:linear-gradient(var(--bar-top),var(--bar-bottom));border-bottom:1px solid #8a6d10;box-sizing:border-box;}
  .toolbar__btn{flex:1;display:flex;align-items:center;justify-content:center;}
  .toolbar__btn + .toolbar__btn{border-left:1px solid #262626;box-shadow:inset 1px 0 #6a6a6a;}

  .well{position:absolute;left:0;right:0;background:var(--panel-dark);box-shadow:inset 0 2px 3px rgba(0,0,0,.5);}

  .t{position:absolute;left:0;right:0;text-align:center;transform:translateY(-50%);line-height:1.1;margin:0;}
  .label{color:var(--label);}
  .digits{font-family:"Mulish",sans-serif;font-weight:900;color:var(--digits);text-shadow:0 2px 3px rgba(0,0,0,.7);letter-spacing:.5px;}
  .stamp{color:var(--date);word-spacing:.4em;}
  .stamp span + span{margin-left:1.2em;}

  .currency{position:absolute;left:0;right:0;transform:translateY(-50%);display:flex;align-items:center;}
  .currency__menu{display:flex;flex-direction:column;justify-content:space-between;}
  .currency__menu i{display:block;background:var(--gold);border-radius:1px;}
  .currency__name{color:var(--row-text);font-family:"Mulish",sans-serif;font-weight:700;flex:1;}
  .flag{display:block;}
  .flag--usd{background:linear-gradient(180deg,#3c4f8f 0%,#c33b3b 35%,#f1eeee 60%,#c33b3b 100%);}
  .flag--mmk{background:linear-gradient(180deg,#f4c300 0%,#f4c300 30%,#3ea641 50%,#3ea641 62%,#d62b2f 85%);}

  .swap{position:absolute;left:50%;transform:translate(-50%,-50%);}

  .ad{position:absolute;left:0;right:0;background:#3a3a3a;}
  .ad__unit{position:absolute;top:0;bottom:0;display:flex;}
  .ad__brand{flex:1;background:var(--ad-dark);display:flex;align-items:center;color:var(--ad-lime);}
  .ad__mark{background:var(--ad-lime);display:block;}
  .ad__name{font-family:"Mulish",sans-serif;font-weight:700;color:var(--ad-lime);}
  .ad__tag{line-height:1;}
  .ad__cta{background:var(--ad-pink);color:#fff;display:flex;align-items:center;line-height:1;}
  .ad__arrow{width:0;height:0;border-left-style:solid;border-right-style:solid;border-top-style:solid;border-left-color:transparent;border-right-color:transparent;border-top-color:#fff;}
  .ad__info{position:absolute;left:2px;bottom:1px;border:1px solid #9a9a9a;border-radius:50%;color:#bbb;text-align:center;font-family:"Mulish",sans-serif;font-weight:700;}
</style>
</head>
<body>

<svg width="0" height="0" style="position:absolute" aria-hidden="true">
  <symbol id="icon-info" viewBox="0 0 24 24">
    <circle cx="12" cy="12" r="10" fill="none" stroke="#f5b400" stroke-width="2.2"/>
    <rect x="10.8" y="10" width="2.4" height="8" fill="#f5b400"/>
    <rect x="10.8" y="5.8" width="2.4" height="2.6" fill="#f5b400"/>
  </symbol>
  <symbol id="icon-refresh" viewBox="0 0 24 24">
    <path d="M19.5 12.5A7.5 7.5 0 1 1 15.5 5.4" fill="none" stroke="#f5b400" stroke-width="2.4"/>
    <polygon points="13,2 21,4.5 15.5,10" fill="#f5b400"/>
  </symbol>
  <symbol id="icon-swap" viewBox="0 0 100 100">
    <g fill="none" stroke="#f5b400" stroke-width="11">
      <path d="M20 50 A30 30 0 0 1 68 26"/>
      <path d="M80 50 A30 30 0 0 1 32 74"/>
    </g>
    <polygon points="56,10 90,26 62,46" fill="#f5b400"/>
    <polygon points="44,90 10,74 38,54" fill="#f5b400"/>
  </symbol>
</svg>

<h2 class="size-title" style="left:124px;width:200px;">1280x720</h2>
<h2 class="size-title" style="left:470px;width:200px;">480x854</h2>
<h2 class="size-title" style="left:750px;width:200px;">480x800</h2>
<h2 class="size-title" style="left:984px;width:200px;">320x480</h2>

<!-- 1280x720 -->
<section class="screen screen--1280">
  <div class="toolbar" style="height:45px;">
    <div class="toolbar__btn"><svg width="25" height="25"><use href="#icon-info"/></svg></div>
    <div class="toolbar__btn"><svg width="25" height="25"><use href="#icon-refresh"/></svg></div>
  </div>
  <p class="t label" style="top:60px;font-size:18px;">amount</p>
  <div class="well" style="top:75px;height:62px;"></div>
  <p class="t digits" style="top:107px;font-size:42px;">8196.75</p>

  <p class="t label" style="top:160px;font-size:18px;">from</p>
  <div class="currency" style="top:191px;height:32px;">
    <span class="currency__menu" style="margin-left:30px;width:26px;height:13px;"><i style="height:3px"></i><i style="height:3px"></i><i style="height:3px"></i></span>
    <span class="currency__name" style="margin-left:10px;font-size:19px;">(USD) U.S. Dollar</span>
    <span class="flag flag--usd" role="img" aria-label="U.S. flag" style="width:43px;height:32px;margin-right:30px;"></span>
  </div>
  <svg class="swap" style="top:278px;" width="95" height="95" role="img" aria-label="Swap currencies"><use href="#icon-swap"/></svg>
  <p class="t label" style="top:366px;font-size:18px;">to</p>
  <div class="currency" style="top:397px;height:32px;">
    <span class="currency__menu" style="margin-left:30px;width:26px;height:13px;"><i style="height:3px"></i><i style="height:3px"></i><i style="height:3px"></i></span>
    <span class="currency__name" style="margin-left:10px;font-size:19px;">(MMK) Myanmar Kyat</span>
    <span class="flag flag--mmk" role="img" aria-label="Myanmar flag" style="width:43px;height:32px;margin-right:30px;"></span>
  </div>
  <p class="t label" style="top:485px;font-size:18px;">converted amount</p>
  <div class="well" style="top:498px;height:128px;"></div>
  <p class="t stamp" style="top:511px;font-size:16px;"><span>21.03.2013</span><span>10:23 PM</span></p>
  <p class="t digits" style="top:563px;font-size:64px;">11362.48</p>

  <div class="ad" style="top:626px;height:55px;">
    <div class="ad__unit" style="left:23px;width:338px;">
      <div class="ad__brand" style="padding-left:10px;gap:8px;">
        <span class="ad__mark" style="width:22px;height:22px;"></span>
        <span class="ad__name" style="font-size:24px;">Chatterly</span>
        <span class="ad__tag" style="font-size:13px;margin-left:2px;">Instant<br>Messenger</span>
      </div>
      <div class="ad__cta" style="width:120px;padding-left:11px;box-sizing:border-box;font-size:16px;gap:14px;">
        <span>Download<br>free app</span>
        <span class="ad__arrow" style="border-left-width:8px;border-right-width:8px;border-top-width:11px;"></span>
      </div>
    </div>
    <span class="ad__info" style="width:13px;height:13px;font-size:9px;line-height:13px;">i</span>
  </div>
</section>

<!-- 480x854 -->
<section class="screen screen--854">
  <div class="toolbar" style="height:30px;">
    <div class="toolbar__btn"><svg width="17" height="17"><use href="#icon-info"/></svg></div>
    <div class="toolbar__btn"><svg width="17" height="17"><use href="#icon-refresh"/></svg></div>
  </div>
  <p class="t label" style="top:40px;font-size:13px;">amount</p>
  <div class="well" style="top:52px;height:38px;"></div>
  <p class="t digits" style="top:71px;font-size:28px;">8196.75</p>

  <p class="t label" style="top:106px;font-size:13px;">from</p>
  <div class="currency" style="top:127px;height:20px;">
    <span class="currency__menu" style="margin-left:20px;width:17px;height:9px;"><i style="height:2px"></i><i style="height:2px"></i><i style="height:2px"></i></span>
    <span class="currency__name" style="margin-left:5px;font-size:14px;">(USD) U.S. Dollar</span>
    <span class="flag flag--usd" role="img" aria-label="U.S. flag" style="width:29px;height:20px;margin-right:20px;"></span>
  </div>
  <svg class="swap" style="top:186px;" width="62" height="62" role="img" aria-label="Swap currencies"><use href="#icon-swap"/></svg>
  <p class="t label" style="top:244px;font-size:13px;">to</p>
  <div class="currency" style="top:265px;height:20px;">
    <span class="currency__menu" style="margin-left:20px;width:17px;height:9px;"><i style="height:2px"></i><i style="height:2px"></i><i style="height:2px"></i></span>
    <span class="currency__name" style="margin-left:5px;font-size:14px;">(MMK) Myanmar Kyat</span>
    <span class="flag flag--mmk" role="img" aria-label="Myanmar flag" style="width:29px;height:20px;margin-right:20px;"></span>
  </div>
  <p class="t label" style="top:324px;font-size:13px;">converted amount</p>
  <div class="well" style="top:333px;height:86px;"></div>
  <p class="t stamp" style="top:341px;font-size:12px;"><span>21.03.2013</span><span>10:23 PM</span></p>
  <p class="t digits" style="top:375px;font-size:44px;">11362.48</p>

  <div class="ad" style="top:419px;height:35px;">
    <div class="ad__unit" style="left:14px;width:227px;">
      <div class="ad__brand" style="padding-left:6px;gap:5px;">
        <span class="ad__mark" style="width:14px;height:14px;"></span>
        <span class="ad__name" style="font-size:16px;">Chatterly</span>
        <span class="ad__tag" style="font-size:9px;">Instant<br>Messenger</span>
      </div>
      <div class="ad__cta" style="width:81px;padding-left:7px;box-sizing:border-box;font-size:11px;gap:9px;">
        <span>Download<br>free app</span>
        <span class="ad__arrow" style="border-left-width:6px;border-right-width:6px;border-top-width:8px;"></span>
      </div>
    </div>
    <span class="ad__info" style="width:10px;height:10px;font-size:7px;line-height:10px;">i</span>
  </div>
</section>

<!-- 480x800 -->
<section class="screen screen--800">
  <div class="toolbar" style="height:30px;">
    <div class="toolbar__btn"><svg width="17" height="17"><use href="#icon-info"/></svg></div>
    <div class="toolbar__btn"><svg width="17" height="17"><use href="#icon-refresh"/></svg></div>
  </div>
  <p class="t label" style="top:40px;font-size:13px;">amount</p>
  <div class="well" style="top:52px;height:38px;"></div>
  <p class="t digits" style="top:71px;font-size:28px;">8196.75</p>

  <p class="t label" style="top:106px;font-size:13px;">from</p>
  <div class="currency" style="top:127px;height:20px;">
    <span class="currency__menu" style="margin-left:20px;width:17px;height:9px;"><i style="height:2px"></i><i style="height:2px"></i><i style="height:2px"></i></span>
    <span class="currency__name" style="margin-left:5px;font-size:14px;">(USD) U.S. Dollar</span>
    <span class="flag flag--usd" role="img" aria-label="U.S. flag" style="width:29px;height:20px;margin-right:20px;"></span>
  </div>
  <svg class="swap" style="top:186px;" width="62" height="62" role="img" aria-label="Swap currencies"><use href="#icon-swap"/></svg>
  <p class="t label" style="top:244px;font-size:13px;">to</p>
  <div class="currency" style="top:265px;height:20px;">
    <span class="currency__menu" style="margin-left:20px;width:17px;height:9px;"><i style="height:2px"></i><i style="height:2px"></i><i style="height:2px"></i></span>
    <span class="currency__name" style="margin-left:5px;font-size:14px;">(MMK) Myanmar Kyat</span>
    <span class="flag flag--mmk" role="img" aria-label="Myanmar flag" style="width:29px;height:20px;margin-right:20px;"></span>
  </div>
  <p class="t label" style="top:295px;font-size:13px;">converted amount</p>
  <div class="well" style="top:303px;height:87px;"></div>
  <p class="t stamp" style="top:312px;font-size:12px;"><span>21.03.2013</span><span>10:23 PM</span></p>
  <p class="t digits" style="top:347px;font-size:44px;">11362.48</p>

  <div class="ad" style="top:390px;height:34px;">
    <div class="ad__unit" style="left:14px;width:227px;">
      <div class="ad__brand" style="padding-left:6px;gap:5px;">
        <span class="ad__mark" style="width:14px;height:14px;"></span>
        <span class="ad__name" style="font-size:16px;">Chatterly</span>
        <span class="ad__tag" style="font-size:9px;">Instant<br>Messenger</span>
      </div>
      <div class="ad__cta" style="width:81px;padding-left:7px;box-sizing:border-box;font-size:11px;gap:9px;">
        <span>Download<br>free app</span>
        <span class="ad__arrow" style="border-left-width:6px;border-right-width:6px;border-top-width:8px;"></span>
      </div>
    </div>
    <span class="ad__info" style="width:10px;height:10px;font-size:7px;line-height:10px;">i</span>
  </div>
</section>

<!-- 320x480 -->
<section class="screen screen--480">
  <div class="toolbar" style="height:20px;">
    <div class="toolbar__btn"><svg width="11" height="11"><use href="#icon-info"/></svg></div>
    <div class="toolbar__btn"><svg width="11" height="11"><use href="#icon-refresh"/></svg></div>
  </div>
  <p class="t label" style="top:24px;font-size:8px;">amount</p>
  <div class="well" style="top:30px;height:25px;"></div>
  <p class="t digits" style="top:42px;font-size:18px;">8196.75</p>

  <p class="t label" style="top:64px;font-size:8px;">from</p>
  <div class="currency" style="top:76px;height:12px;">
    <span class="currency__menu" style="margin-left:20px;width:10px;height:6px;"><i style="height:1.4px"></i><i style="height:1.4px"></i><i style="height:1.4px"></i></span>
    <span class="currency__name" style="margin-left:6px;font-size:8px;">(USD) U.S. Dollar</span>
    <span class="flag flag--usd" role="img" aria-label="U.S. flag" style="width:17px;height:12px;margin-right:20px;"></span>
  </div>
  <svg class="swap" style="top:110px;" width="32" height="32" role="img" aria-label="Swap currencies"><use href="#icon-swap"/></svg>
  <p class="t label" style="top:146px;font-size:7px;">to</p>
  <div class="currency" style="top:158px;height:12px;">
    <span class="currency__menu" style="margin-left:20px;width:10px;height:6px;"><i style="height:1.4px"></i><i style="height:1.4px"></i><i style="height:1.4px"></i></span>
    <span class="currency__name" style="margin-left:6px;font-size:8px;">(MMK) Myanmar Kyat</span>
    <span class="flag flag--mmk" role="img" aria-label="Myanmar flag" style="width:17px;height:12px;margin-right:20px;"></span>
  </div>
  <p class="t label" style="top:178px;font-size:7px;">converted amount</p>
  <div class="well" style="top:183px;height:52px;"></div>
  <p class="t stamp" style="top:188px;font-size:6px;"><span>21.03.2013</span><span>10:23 PM</span></p>
  <p class="t digits" style="top:210px;font-size:24px;">11362.48</p>

  <div class="ad" style="top:235px;height:21px;">
    <div class="ad__unit" style="left:27px;width:135px;">
      <div class="ad__brand" style="padding-left:4px;gap:3px;">
        <span class="ad__mark" style="width:8px;height:8px;"></span>
        <span class="ad__name" style="font-size:10px;">Chatterly</span>
        <span class="ad__tag" style="font-size:5px;">Instant<br>Messenger</span>
      </div>
      <div class="ad__cta" style="width:48px;padding-left:4px;box-sizing:border-box;font-size:6px;gap:5px;">
        <span>Download<br>free app</span>
        <span class="ad__arrow" style="border-left-width:3.5px;border-right-width:3.5px;border-top-width:5px;"></span>
      </div>
    </div>
    <span class="ad__info" style="width:7px;height:7px;font-size:5px;line-height:7px;">i</span>
  </div>
</section>

</body>
</html>
```